Technology solutions catalog

Were looking for a catalogue to supplement our website and corporate branding.

Our website will give you a good understanding of our products and services as well as our theme.

Our base colour and logo is red, white and grey.

www.voltrane.com.au

The aim of the catalogue is to showcase our business IT services & solutions. This will be a mix of education about the new solutions available to small and medium business today and how these solutions can increase productivity.

We would also like tip sections

This isn't all about selling but also about educating SMB's of the new and exciting IT solutions available today and having them book a free consult with us to discuss further about how we can help the business.

Solutions and area's that the catalogue will need to cover include

Front Cover -
-About us section, with our business contact information (1st page)
- Introduction. (2nd page)
-Communication Solutions - this includes Email, IP phones and business IT networks (2 pages)
- Data & Storage solutions (2 pages)
- Hardware (1 pages)
- Business IT health check list (1 page)
- Services and support offering (2 pages)
- Software & Popular cloud solutions (2 pages)
- Website / E-commerce solutions (2 pages)
Back cover

Based on two pages per solution the whole catalogue will be around 14 pages.

We don't need any text content done. We would like Headings on pages including page numbers. Footer please.

We're looking for a template that we can have our designer finish off by adding in some further product and service image and text.

Thank you for your consideration

Target Market(s)

IT for small and medium businesses

Industry/Entity Type

Supplement

Requirements
Must have
• Size A4
• Design supplied in Adobe indesign so we can edit and add our text and content
• Clean design

```html
<!DOCTYPE html>
<html lang="en">
<head>
<meta charset="utf-8">
<title>About Voltrane – Catalogue Spread</title>
<link rel="stylesheet" href="https://fonts.googleapis.com/css2?family=Source+Sans+3:wght@400;700&display=swap">
<style>
  :root {
    --backdrop: #e9e6e1;
    --page: #ffffff;
    --brand-red: #b3161e;
    --text-grey: #4f4f4f;
    --photo-light: #a9d8e6;
    --photo-mid: #6fa6cf;
    --photo-deep: #2c4f9a;
  }
  html, body {
    margin: 0;
    width: 1200px;
    height: 1200px;
    overflow: hidden;
    background: var(--backdrop);
    font-family: "Source Sans 3", "Myriad Pro", Arial, sans-serif;
  }
  .spread {
    position: absolute;
    left: 50px;
    top: 211px;
    width: 1100px;
    height: 778px;
    display: flex;
    box-shadow: 0 4px 14px rgba(0,0,0,0.18);
  }
  .page-photo {
    width: 550px;
    height: 100%;
    background:
      radial-gradient(circle at 30% 40%, var(--photo-deep) 0%, transparent 45%),
      linear-gradient(135deg, var(--photo-mid) 0%, var(--photo-light) 55%, #cdebf2 100%);
  }
  .page-about {
    position: relative;
    width: 550px;
    height: 100%;
    background: var(--page);
  }
  .about-content {
    position: absolute;
    left: 55px;
    top: 318px;
    width: 440px;
    color: var(--text-grey);
    font-size: 16.5px;
    line-height: 20.2px;
  }
  .about-title {
    margin: 0 0 22px;
    color: var(--brand-red);
    font-weight: 700;
    font-size: 30px;
    line-height: 1.2;
    letter-spacing: -0.2px;
  }
  .about-content p { margin: 0; }
  .industry-list {
    list-style: none;
    margin: 18px 0 18px;
    padding: 0;
    color: var(--brand-red);
  }
  .industry-list li {
    position: relative;
    padding-left: 25px;
  }
  .industry-list li::before {
    content: "";
    position: absolute;
    left: 0;
    top: 6px;
    width: 8px;
    height: 8px;
    background: var(--brand-red);
  }
</style>
</head>
<body>
  <main class="spread">
    <div class="page-photo" role="img" aria-label="Photo of a businessman in a suit holding a tablet, overlaid with glowing network lines and light bokeh in blue tones"></div>
    <section class="page-about">
      <div class="about-content">
        <h1 class="about-title">About Voltrane</h1>
        <p>Founded in late 2009. Voltrane Business is a small, customer focused information technology company that focuses on helping small medium businesses increase productivity through simple and effective technology solutions Industries we have experience servicing and supporting:</p>
        <ul class="industry-list">
          <li>Medical &nbsp;– &nbsp;Psychology, Dental &amp; General Practice.</li>
          <li>Hospitality – Hotels, Restaurants &amp; Cafes</li>
          <li>Retail &amp; E-commerce</li>
          <li>Professional Services</li>
          <li>Trade Services</li>
        </ul>
        <p>From the onset we wanted to provide small and medium business with great service, leading information technology solutions that were simple, effective and affordable.</p>
      </div>
    </section>
  </main>
</body>
</html>
```